10' Banner for Pest Control Company

I need a 10'x10' banner created for a Pest Control Company named, Brightfield Pest Control. It is a total service company so equal emphasis needs to be placed on bugs, termites, rodents, weeds, and tree services like Olive Tree spraying for fruit suppression. The main colors are Orange and Grey. This will be a banner for use at trade shows. It needs to show a customer at a glance exactly what we do and what our name is.
Our website is under development at http://dev.marlowbeck-example.com so you can visit there and get an idea of the colors used.
Thank you!
Updates

Project Deadline Extended
Reason: Deadline extended per some designer's requests.

Target Market(s)

People looking for pest control services in Phoenix, Arizona

Industry/Entity Type

Pest Control

Requirements
Must have
• Photos of pests.. bugs, rodents, termites, weeds, tree spraying
• Large logo
• Vibrant and eye catching

```html
<!DOCTYPE html>
<html lang="en">
<head>
<meta charset="utf-8">
<title>Brightfield Pest Control – Trade Show Banner</title>
<link href="https://fonts.googleapis.com/css2?family=Archivo+Black&family=Lato:wght@400;700&display=swap" rel="stylesheet">
<style>
  :root {
    --orange: #e8612a;
    --grey: #8f8f8f;
    --grey-dark: #7d7d7d;
    --white: #ffffff;
    --stripe: #a9a9a9;
  }
  * { box-sizing: border-box; margin: 0; padding: 0; }
  html, body { width: 1200px; height: 1107px; overflow: hidden; background: var(--white); }
  .banner {
    width: 1200px; height: 1107px;
    display: flex; flex-direction: column;
    font-family: "Archivo Black", sans-serif;
  }
  .brand-area {
    height: 300px; background: var(--white);
    display: flex; align-items: center; justify-content: center;
    border-bottom: 12px solid var(--stripe);
  }
  .brand { display: flex; align-items: center; gap: 22px; }
  .brand-mark {
    width: 54px; height: 54px; border-radius: 50%;
    background: var(--orange); flex: none;
  }
  .brand-name {
    color: var(--orange);
    font-size: 62px; line-height: 1.02; letter-spacing: 1px;
    text-transform: uppercase;
  }
  .services {
    flex: 1; background: var(--orange);
    padding: 32px 40px 30px;
    display: flex; flex-direction: column;
  }
  .headline {
    color: var(--white);
    text-align: center; text-transform: uppercase;
    font-size: 44px; line-height: 1.2; letter-spacing: 2px;
    margin-bottom: 30px;
  }
  .photo-grid {
    flex: 1;
    display: grid;
    grid-template-columns: repeat(3, 1fr);
    grid-template-rows: repeat(2, 1fr);
    gap: 20px 24px;
  }
  .photo { border: 2px solid rgba(255,255,255,0.55); }
  .photo--aphids { background: linear-gradient(160deg, #1b2447 0%, #24305a 45%, #b8cf52 75%, #d8e07a 100%); }
  .photo--beetle { background: radial-gradient(ellipse at 50% 45%, #1f8a3a 0%, #2c6e2f 25%, #8a8378 60%, #b3aca0 100%); }
  .photo--roach { background: radial-gradient(ellipse at 45% 40%, #8e3c16 0%, #b5651d 25%, #f4f4f2 60%, #e6e6e4 100%); }
  .photo--mouse { background: linear-gradient(135deg, #2e3f7a 0%, #5d4a3c 40%, #7a5a3e 70%, #d9c6a8 100%); }
  .photo--termite { background: radial-gradient(ellipse at 55% 50%, #5a2e1c 0%, #b87a3c 35%, #d6b27a 70%, #c4a05e 100%); }
  .photo--spraying { background: radial-gradient(ellipse at 65% 45%, #f2f2f2 0%, #e0e0e0 18%, #4e7f2a 45%, #3b6b22 100%); }
  .contact-area {
    height: 227px; background: var(--grey);
    display: flex; flex-direction: column; align-items: center; justify-content: center;
    gap: 26px;
  }
  .website {
    font-family: "Lato", sans-serif; font-weight: 700;
    color: var(--white); font-size: 46px; letter-spacing: 0.5px;
  }
  .social { display: flex; gap: 10px; }
  .social-dot {
    width: 38px; height: 38px; border-radius: 50%;
    background: var(--white);
  }
</style>
</head>
<body>
  <main class="banner">
    <header class="brand-area">
      <div class="brand">
        <span class="brand-mark" aria-hidden="true"></span>
        <h1 class="brand-name">Brightfield<br>Pest Control</h1>
      </div>
    </header>

    <section class="services">
      <h2 class="headline">Safe and Effective<br>Pest Control Solutions</h2>
      <div class="photo-grid">
        <div class="photo photo--aphids" role="img" aria-label="Photo of green aphids on a plant stem"></div>
        <div class="photo photo--beetle" role="img" aria-label="Photo of a metallic green beetle"></div>
        <div class="photo photo--roach" role="img" aria-label="Photo of a cockroach on a white surface"></div>
        <div class="photo photo--mouse" role="img" aria-label="Photo of a mouse peeking out of a hole in a wall"></div>
        <div class="photo photo--termite" role="img" aria-label="Photo of a termite on wood"></div>
        <div class="photo photo--spraying" role="img" aria-label="Photo of a technician in protective suit spraying trees"></div>
      </div>
    </section>

    <footer class="contact-area">
      <p class="website">www.dev.marlowbeck-example.com</p>
      <div class="social" aria-label="Social media">
        <span class="social-dot"></span>
        <span class="social-dot"></span>
        <span class="social-dot"></span>
        <span class="social-dot"></span>
      </div>
    </footer>
  </main>
</body>
</html>
```